MS word document templates for consultancy

I need the following templates for my business using my logo as branding.

- General report template
- Letter head template
- Tender proposal template

The templates should be sleek and with minimal colors, but with a small amount of green and grey where appropriate (as per attached logo and email signature). Font should be consistent with the text in the email signature.

```html
<!DOCTYPE html>
<html lang="en">
<head>
<meta charset="utf-8">
<title>Northway Group Letterhead</title>
<link href="https://fonts.googleapis.com/css2?family=Lato:wght@400;700&family=Kaushan+Script&display=swap" rel="stylesheet">
<style>
  :root {
    --canvas: #ffffff;
    --paper: #f2f1f5;
    --ink: #3a3a3a;
    --brand-ink: #141414;
    --bar: #111111;
    --green: #23944a;
  }
  * { margin: 0; padding: 0; box-sizing: border-box; }
  html, body {
    width: 1152px; height: 1200px; overflow: hidden;
    background: var(--canvas);
    font-family: "Lato", Arial, sans-serif;
    color: var(--ink);
  }
  .letterhead {
    position: absolute; left: 166px; top: 30px;
    width: 819px; height: 1140px;
    background: var(--paper);
  }
  .side-bar {
    position: absolute; left: 0; top: 0; width: 24px; height: 100%;
    background: var(--bar);
  }
  .side-bar-accent {
    position: absolute; left: 0; top: 1036px; width: 24px; height: 70px;
    background: var(--green);
    border-top: 3px solid var(--paper);
    border-bottom: 3px solid var(--paper);
  }
  .brand {
    position: absolute; left: 46px; top: 56px;
    display: flex; align-items: center; gap: 12px;
    font-size: 42px; font-weight: 400; color: var(--brand-ink);
    letter-spacing: 0.5px;
  }
  .brand-square { width: 14px; height: 14px; background: var(--green); }
  .block { position: absolute; left: 54px; font-size: 16px; line-height: 19px; }
  .date { top: 246px; }
  .recipient { top: 285px; }
  .company { top: 341px; }
  .greeting { top: 424px; font-size: 19px; font-weight: 700; }
  .body-text {
    position: absolute; left: 54px; width: 712px;
    font-size: 15px; line-height: 18px; text-align: justify;
  }
  .p1 { top: 548px - 80px; }
  .closing { top: 790px; }
  .signature {
    position: absolute; left: 56px; top: 830px;
    font-family: "Kaushan Script", cursive; font-size: 36px; color: #2a2a2a;
  }
  .sender {
    position: absolute; left: 40px; top: 1036px;
    font-size: 16px; line-height: 23px;
  }
  .phone { display: flex; align-items: center; gap: 6px; margin-top: 7px; }
</style>
</head>
<body>
  <main class="letterhead">
    <div class="side-bar"></div>
    <div class="side-bar-accent"></div>

    <header class="brand"><span>Northway Group</span><span class="brand-square"></span></header>

    <p class="block date">Jun-03-2021</p>
    <p class="block recipient">Mr, Peter Lane<br>President</p>
    <p class="block company">Crestline Corporation<br>45 Harbour Road, Suite# 12<br>City, State, 120023</p>
    <p class="block greeting">Dear Mr, Peter</p>

    <p class="body-text" style="top:460px">Lorem ipsum dolor sit amet, consectetur adipisicing elit, sed do eiusmod tempor incididunt ut labore et dolore magna aliqua. Ut enim ad minim veniam, quis nostrud exercitation ullamco laboris nisi ut aliquip ex ea commodo consequat. Duis aute irure dolor in reprehenderit in voluptate velit esse cillum dolore eu fugiat nulla pariatur.</p>
    <p class="body-text" style="top:549px">Lorem ipsum dolor sit amet, consectetur adipisicing elit, sed do eiusmod tempor incididunt ut labore et dolore magna aliqua. Ut enim ad minim veniam, quis nostrud exercitation ullamco laboris nisi ut aliquip ex ea commodo consequat. Duis aute irure dolor in reprehenderit in voluptate velit esse cillum dolore eu fugiat nulla pariatur.</p>
    <p class="body-text" style="top:638px">Lorem ipsum dolor sit amet, consectetur adipisicing elit, sed do eiusmod tempor incididunt ut labore et dolore magna aliqua. Ut enim ad minim veniam, quis nostrud exercitation ullamco laboris nisi ut aliquip ex ea commodo consequat.</p>
    <p class="body-text" style="top:710px">Excepteur sint occaecat cupidatat non proident, sunt in culpa qui officia deserunt mollit anim id est laborum. re et dolore magnam aliquam quaerat voluptatem.</p>

    <p class="block closing">Regards</p>
    <p class="signature">Owen Carter</p>

    <footer class="sender">
      <p>Daniel Reeve</p>
      <p>Managing Director</p>
      <p class="phone">
        <svg width="14" height="14" viewBox="0 0 24 24" aria-hidden="true"><path fill="var(--green)" d="M6.6 10.8a15.1 15.1 0 0 0 6.6 6.6l2.2-2.2a1 1 0 0 1 1-.25 11.4 11.4 0 0 0 3.6.57 1 1 0 0 1 1 1V20a1 1 0 0 1-1 1A17 17 0 0 1 3 4a1 1 0 0 1 1-1h3.5a1 1 0 0 1 1 1c0 1.25.2 2.45.57 3.57a1 1 0 0 1-.25 1z"/></svg>
        <span>0400 555 019</span>
      </p>
    </footer>
  </main>
</body>
</html>
```